Kettle Ledger Business Card design

We need a stand out business card design for Accounting practice based in Australia specialising in pubs, clubs and hotels. We help venues maximise margins, create time and manage cashflow. One club we have been working with for the last 6 months has increased revenue by 3% and margin by 5% in this time frame. We have a back office outsourced system that costs less than having a full time employee and also allows the venues the added benefit of:<br/>-using the office space to become a revenue generating opportunity. <br/>-a complete system to enhance governance, accountability and efficiency within their operation<br/>-52 weeks cover so no hassle to cover annual/sick .. leave<br/><br/>We would like to see designs that use the colours of our logo (green & blue).
Target Market(s)
Australian Pubs, Clubs & Hotels abookkeeping, accounting and tax services
Industry/Entity Type
Accountant
Contact Information for Business Card
Miriam Oakley CPA
Principal
Accountant Tax Agent
Miriam@KettleLedger-example.com.au
0418693142
www.kettleledger-example.com.au
Accounting / Payroll / Tax / SMSF / Technology
Colors
Designer to choose colors to be used in the design.
Look and feel
Each slider illustrates characteristics of the customer's brand and the style your logo design should communicate.

```html
<!DOCTYPE html>
<html lang="en">
<head>
<meta charset="utf-8">
<title>Kettle Ledger – Business Card</title>
<link rel="stylesheet" href="https://fonts.googleapis.com/css2?family=Source+Sans+3:wght@400;600;700&display=swap">
<style>
  :root {
    --canvas: #c9c9c9;
    --paper: #ffffff;
    --brand-blue: #22418f;
    --brand-green: #0f7340;
    --accent-grey: #d4d4d8;
    --ink: #1a1a1a;
    --badge-dark: #111111;
    --badge-light: #cfcfcf;
  }
  html, body {
    margin: 0;
    padding: 0;
    width: 1200px;
    height: 1200px;
    overflow: hidden;
    background: var(--canvas);
  }
  .canvas {
    position: relative;
    width: 1200px;
    height: 1200px;
  }
  .card {
    position: absolute;
    left: 217px;
    width: 765px;
    height: 437px;
    background: var(--paper);
  }
  .card--front { top: 124px; }
  .card--back { top: 641px; }
  .card svg {
    display: block;
    width: 100%;
    height: 100%;
    font-family: "Source Sans 3", sans-serif;
  }
  .band-blue { fill: var(--brand-blue); }
  .band-green { fill: var(--brand-green); }
  .band-grey { fill: var(--accent-grey); }
  .person-name { fill: var(--brand-blue); font-size: 40px; font-weight: 400; }
  .person-name .given { font-weight: 700; }
  .person-role { fill: var(--brand-green); font-size: 33px; font-weight: 400; }
  .person-title { fill: var(--brand-green); font-size: 28px; font-weight: 400; }
  .wordmark { fill: var(--brand-blue); font-weight: 700; }
  .wordmark--front { font-size: 44px; }
  .wordmark--back { font-size: 58px; }
  .contact { fill: var(--ink); font-size: 27px; font-weight: 400; }
  .contact--web { fill: var(--paper); }
  .services { fill: var(--paper); font-size: 26px; font-weight: 400; }
  .icon-box--green { fill: var(--brand-green); }
  .icon-box--blue { fill: var(--brand-blue); }
  .icon-box--outline { fill: none; stroke: var(--paper); stroke-width: 2; }
  .icon-line { fill: none; stroke: var(--paper); stroke-width: 2.5; }
  .icon-fill { fill: var(--paper); }
  .badge-dark { fill: var(--badge-dark); }
  .badge-light { fill: var(--badge-light); }
</style>
</head>
<body>
<main class="canvas">

  <section class="card card--front" aria-label="Business card front">
    <svg viewBox="0 0 1020 582" xmlns="http://www.w3.org/2000/svg">
      <g class="identity">
        <text class="person-name" x="79" y="101"><tspan class="given">Miriam</tspan> Oakley CPA</text>
        <text class="person-role" x="79" y="142">Principal</text>
        <text class="person-title" x="79" y="174">Accountant Tax Agent</text>
      </g>

      <text class="wordmark wordmark--front" x="956" y="150" text-anchor="end">Kettle Ledger</text>

      <g class="contact-list">
        <text class="contact" x="882" y="356" text-anchor="end">0418693142</text>
        <rect class="icon-box--green" x="902" y="324" width="54" height="48"/>
        <rect class="icon-line" x="920" y="333" width="18" height="30" rx="3"/>
        <circle class="icon-fill" cx="929" cy="358" r="1.8"/>

        <text class="contact" x="882" y="419" text-anchor="end">Miriam@KettleLedger-example.com.au</text>
        <rect class="icon-box--blue" x="902" y="387" width="54" height="50"/>
        <rect class="icon-line" x="913" y="401" width="32" height="22"/>
        <polyline class="icon-line" points="913,401 929,414 945,401"/>
        <polyline class="icon-line" points="913,423 925,411"/>
        <polyline class="icon-line" points="945,423 933,411"/>
      </g>

      <g class="bands">
        <polygon class="band-grey" points="0,338 140,456 119,456 0,356"/>
        <polygon class="band-blue" points="0,356 119,456 178,456 219,491 451,491 483,520 1020,520 1020,582 0,582"/>
        <polygon class="band-green" points="119,456 178,456 325,582 266,582"/>
        <polygon class="band-green" points="0,458 146,582 0,582"/>
        <polygon class="band-green" points="407,450 1020,450 1020,520 483,520"/>
      </g>

      <g class="contact-web">
        <text class="contact contact--web" x="882" y="495" text-anchor="end">www.kettleledger-example.com.au</text>
        <rect class="icon-box--outline" x="902" y="461" width="54" height="50"/>
        <circle class="icon-fill" cx="929" cy="486" r="13"/>
        <line x1="916" y1="486" x2="942" y2="486" stroke="var(--brand-green)" stroke-width="1.5"/>
        <line x1="929" y1="473" x2="929" y2="499" stroke="var(--brand-green)" stroke-width="1.5"/>
        <ellipse cx="929" cy="486" rx="6" ry="13" fill="none" stroke="var(--brand-green)" stroke-width="1.5"/>
      </g>
    </svg>
  </section>

  <section class="card card--back" aria-label="Business card back">
    <svg viewBox="0 0 1020 582" xmlns="http://www.w3.org/2000/svg">
      <text class="wordmark wordmark--back" x="510" y="248" text-anchor="middle">Kettle Ledger</text>

      <g class="accreditations" aria-label="Professional accreditation badges">
        <rect class="badge-dark" x="361" y="363" width="96" height="37"/>
        <circle class="badge-light" cx="512" cy="381" r="19"/>
        <rect class="badge-light" x="614" y="364" width="34" height="34"/>
      </g>

      <g class="bands">
        <polygon class="band-grey" points="0,338 140,456 119,456 0,356"/>
        <polygon class="band-blue" points="0,356 119,456 178,456 219,491 451,491 483,520 1020,520 1020,582 0,582"/>
        <polygon class="band-green" points="119,456 178,456 325,582 266,582"/>
        <polygon class="band-green" points="0,458 146,582 0,582"/>
        <polygon class="band-green" points="407,450 1020,450 1020,520 483,520"/>
      </g>

      <text class="services" x="741" y="497" text-anchor="middle">Accounting / Payroll / Tax / SMSF / Technology</text>
    </svg>
  </section>

</main>
</body>
</html>
```